New flyer / Software product / Data model finder

New flyer design for a new company based in Stuttgart Germany.

The design should display the product and the companies core values:
Values:
User-friendliness, Costumer Support, Environmental friendliness

Product:
Licensed software framework:

Key software components:
- find models within obtained data or created models
- model dynamic systems
- create extensions

Target Market(s)

Universities, Data mining, Manufacturing industries, Space, Robotics, etc.

Industry/Entity Type

It Company

Colors
0592cd

Requirements
Nice to have
• The companies website is at:
• http://www.brelvan.com/
• It is not obligated to follow the unprofessional self-made alpha design. A design easy to understand and looking good suits. However it will be shown to other people to validate its natural appealing look.
• colors should be: green, blue or something that looks good for the average person.

```html
<!DOCTYPE html>
<html lang="en">
<head>
<meta charset="utf-8">
<title>Brelvan UG – Flyer</title>
<link href="https://fonts.googleapis.com/css2?family=Open+Sans:wght@400;600;700&display=swap" rel="stylesheet">
<style>
  :root {
    --stage: #e9e9e9;
    --beige-dark: #cfc8c0;
    --beige-light: #f3f1ee;
    --paper: #f7f6f3;
    --ink: #2a2a2a;
    --ink-soft: #6d6a66;
    --white: #ffffff;
    --orange-light: #f9a12a;
    --orange: #f37021;
    --orange-deep: #ee5a1c;
    --purple: #5c2160;
    --purple-deep: #3b0d44;
  }
  * { box-sizing: border-box; margin: 0; padding: 0; }
  html, body { width: 1200px; height: 987px; overflow: hidden; }
  body {
    background: var(--stage);
    font-family: "Open Sans", Arial, sans-serif;
    display: flex; align-items: center; justify-content: center;
  }
  .flyer {
    position: relative;
    width: 664px; height: 940px;
    background: var(--paper);
    overflow: hidden;
    box-shadow: 0 6px 24px rgba(0,0,0,.18);
  }
  .hero {
    position: absolute; left: 0; top: 0; width: 100%; height: 560px;
    background: linear-gradient(160deg, var(--beige-dark) 0%, var(--beige-light) 70%);
  }
  .hero-photo {
    position: absolute; left: 210px; top: 60px; width: 270px; height: 500px;
    background: radial-gradient(ellipse at 50% 35%, #b9a597 0%, #cfc6c4 45%, rgba(230,228,232,0) 75%);
  }
  .brand {
    position: absolute; left: 40px; top: 120px;
    font-size: 34px; font-weight: 600; color: var(--white);
    letter-spacing: .5px;
  }
  .intro {
    position: absolute; left: 40px; top: 178px; width: 200px;
    font-size: 11px; line-height: 1.45; color: var(--white);
  }
  .intro p + p { margin-top: 8px; }
  .value-icons { position: absolute; left: 40px; top: 290px; }
  .values {
    position: absolute; right: 36px; top: 40px; width: 170px;
    font-size: 10px; line-height: 1.7; color: var(--ink-soft);
  }
  .values h3 { font-size: 11px; font-weight: 700; margin-bottom: 4px; }
  .values ul { list-style: none; }
  .values li::before { content: "• "; }
  .arrow-curve { position: absolute; right: 150px; top: 160px; }
  .components-card {
    position: absolute; left: 200px; top: 395px; width: 300px;
    padding: 16px 22px 18px;
    background: rgba(255,255,255,.82);
    color: var(--ink);
  }
  .components-card h2 { font-size: 19px; font-weight: 700; margin-bottom: 6px; }
  .tick-list { list-style: none; font-size: 14px; line-height: 1.4; }
  .tick-list li { position: relative; padding-left: 18px; }
  .tick-list li::before {
    content: "✔"; position: absolute; left: 0; font-size: 11px; top: 2px;
  }
  .band-white {
    position: absolute; left: 0; top: 560px; width: 100%; height: 20px; background: var(--white);
  }
  .band-orange {
    position: absolute; left: 0; top: 580px; width: 100%; height: 170px;
    background: linear-gradient(90deg, var(--orange-deep) 0%, var(--orange) 45%, var(--orange-light) 100%);
    display: flex; padding: 26px 30px; gap: 24px;
  }
  .info-col { flex: 1; display: flex; gap: 14px; color: var(--white); }
  .info-col h3 { font-size: 15px; font-weight: 700; color: var(--purple-deep); }
  .info-col p { font-size: 13px; line-height: 1.35; margin-bottom: 8px; }
  .info-col .tick-list { font-size: 13px; color: var(--white); }
  .info-icon { flex: 0 0 34px; }
  .band-purple {
    position: absolute; left: 0; top: 750px; width: 100%; height: 190px;
    background: linear-gradient(135deg, var(--purple) 0%, var(--purple-deep) 100%);
    color: var(--white); text-align: center; padding-top: 46px;
  }
  .contact-web { font-size: 18px; font-weight: 700; }
  .contact-phone { font-size: 22px; font-weight: 700; margin-top: 4px; }
  .legal { font-size: 11px; line-height: 1.5; margin-top: 14px; opacity: .85; }
</style>
</head>
<body>
<main class="flyer">
  <section class="hero">
    <div class="hero-photo" role="img" aria-label="Photo of a smiling businesswoman with long brown hair in a light grey blazer, arms crossed"></div>

    <div class="brand">Brelvan UG</div>
    <div class="intro">
      <p>Brelvan UG is focusing on industry solutions in the field of automation and manufacturing.</p>
      <p>The enhancement of offline robot programming is our main focus.</p>
    </div>

    <svg class="value-icons" width="170" height="80" viewBox="0 0 170 80" aria-hidden="true">
      <g fill="none" stroke="#fff" stroke-width="2">
        <circle cx="20" cy="50" r="17"/>
        <circle cx="75" cy="25" r="17"/>
        <circle cx="130" cy="25" r="17"/>
      </g>
      <g fill="#fff">
        <rect x="13" y="41" width="2" height="18"/>
        <path d="M15 41 h13 l-3 4 3 4 h-13z"/>
        <path d="M69 31 q0-12 6-12 q6 0 6 12 l2 2 h-16z"/>
        <circle cx="75" cy="35" r="2"/>
        <circle cx="125" cy="21" r="3.5"/><circle cx="135" cy="21" r="3.5"/>
        <path d="M118 33 q0-8 7-8 q7 0 7 8z"/><path d="M128 33 q0-8 7-8 q7 0 7 8z"/>
      </g>
      <path d="M60 78 q40-10 100-2" fill="none" stroke="#fff" stroke-width="2"/>
    </svg>

    <div class="values">
      <h3>Core values</h3>
      <ul>
        <li>User-friendly workflow design</li>
        <li>Dedicated customer support</li>
        <li>Environmentally friendly approach</li>
        <li>Open licensed framework</li>
      </ul>
    </div>
    <svg class="arrow-curve" width="40" height="50" viewBox="0 0 40 50" aria-hidden="true">
      <path d="M8 45 q22-8 20-38" fill="none" stroke="#fff" stroke-width="2.5"/>
      <path d="M20 12 l8-8 6 10" fill="none" stroke="#fff" stroke-width="2.5"/>
    </svg>

    <div class="components-card">
      <h2>Key software components:</h2>
      <ul class="tick-list">
        <li>find models within obtained data or created models</li>
        <li>model dynamic systems</li>
        <li>create extensions</li>
      </ul>
    </div>
  </section>

  <div class="band-white"></div>

  <section class="band-orange">
    <div class="info-col">
      <svg class="info-icon" width="34" height="34" viewBox="0 0 34 34" aria-hidden="true">
        <circle cx="17" cy="17" r="15" fill="none" stroke="#fff" stroke-width="2"/>
        <path d="M17 8 a6 6 0 0 1 4 10.5 v3 h-8 v-3 A6 6 0 0 1 17 8z" fill="#fff"/>
        <rect x="13.5" y="23" width="7" height="2" fill="#fff"/>
      </svg>
      <div>
        <h3>Current software product layout:</h3>
        <p>Is completely open, right now it is a black box.</p>
        <h3>Supported Platforms:</h3>
        <p>Windows &amp; Linux</p>
      </div>
    </div>
    <div class="info-col">
      <svg class="info-icon" width="34" height="34" viewBox="0 0 34 34" aria-hidden="true">
        <circle cx="17" cy="17" r="15" fill="none" stroke="#fff" stroke-width="2"/>
        <path d="M17 8 a6 6 0 0 1 4 10.5 v3 h-8 v-3 A6 6 0 0 1 17 8z" fill="#fff"/>
        <rect x="13.5" y="23" width="7" height="2" fill="#fff"/>
      </svg>
      <div>
        <h3>Key software components:</h3>
        <ul class="tick-list">
          <li>find models within obtained data or created models</li>
          <li>model dynamic systems</li>
          <li>create extensions</li>
        </ul>
      </div>
    </div>
  </section>

  <footer class="band-purple">
    <div class="contact-web">info@brelvan.com | www.brelvan.com</div>
    <div class="contact-phone">Call: (+0049 711) 5550 2718</div>
    <div class="legal">
      Angaben gemäß § 5 TMG:<br>
      UG (haftungsbeschränkt) Lindenweg 12, 73728 Esslingen
    </div>
  </footer>
</main>
</body>
</html>
```